Web Design Corvane Mart is a market place for handcrafts products

design a landing home page , and a product page ,
for a market place CMS that will sell handcrafts ..

Target Market(s)

Market place for Handicrafts makers

Number of Pages Required

2 page

Requirements
Nice to have
• Search Google images for Marrakech Saffron Quarter , and Istanbul Copperleaf Arcade

```html
<!DOCTYPE html>
<html lang="en">
<head>
<meta charset="utf-8">
<title>Corvane Mart – Handcraft Marketplace</title>
<link href="https://fonts.googleapis.com/css2?family=Cinzel:wght@400;700&family=Roboto:wght@400;500;700&display=swap" rel="stylesheet">
<style>
:root{
  --accent:#c61f3d;
  --accent-dark:#8e1230;
  --cream:#fbf2ea;
  --ink:#1c1c1c;
  --muted:#666;
  --footer:#161616;
  --star:#f2a81d;
  --purple:#6a1be0;
  --orange:#f0760e;
  --teal:#1793b8;
}
*{box-sizing:border-box;margin:0;padding:0}
html,body{width:1200px;height:5140px;overflow:hidden}
body{background:var(--cream);font-family:'Roboto',sans-serif;color:var(--ink);font-size:14px;position:relative}
a{color:inherit;text-decoration:none}
.serif{font-family:'Cinzel',serif}
.section-title{font-family:'Cinzel',serif;font-weight:700;font-size:38px;text-align:center;letter-spacing:1px}
.btn{display:inline-block;background:var(--accent);color:#fff;font-weight:700;font-size:13px;padding:12px 26px;border-radius:4px;letter-spacing:.5px}
.photo{display:block}

/* top bar */
.topbar{height:40px;background:var(--accent-dark);color:#fff;font-size:13px;display:flex;align-items:center;justify-content:space-between;padding:0 28px}
.topbar .links{display:flex;gap:34px;font-weight:700}
.topbar .links span{display:flex;align-items:center;gap:7px}

/* header */
.header{height:120px;background:#fff;position:relative}
.logo{position:absolute;left:36px;top:22px;display:flex;align-items:center;gap:12px}
.logo .mark{width:60px;height:60px;border-radius:50%;background:var(--accent)}
.logo .name{font-family:'Cinzel',serif;font-size:30px;font-weight:700;color:var(--ink)}
.search{position:absolute;left:596px;top:20px;width:352px;height:40px;border:1px solid #ccc;border-radius:4px;display:flex;overflow:hidden}
.search span{flex:1;padding:11px 14px;color:#999;font-size:13px}
.search b{width:42px;background:var(--accent);display:flex;align-items:center;justify-content:center}
.cart{position:absolute;left:960px;top:20px;display:flex;gap:8px;align-items:center;font-size:12px;font-weight:700}
.cart small{display:block;font-weight:400;color:var(--muted)}
.nav{position:absolute;right:36px;top:84px;display:flex;font-size:14px;font-weight:700}
.nav a{padding:0 22px;border-left:1px solid #999}
.nav a:first-child{border-left:0}

/* hero */
.hero{height:600px;position:relative;background:linear-gradient(120deg,#4a2a1e 0%,#7a3c22 25%,#2b5f86 45%,#a33a2a 65%,#3c2a20 100%)}
.hero .shade{position:absolute;inset:0;background:linear-gradient(90deg,rgba(0,0,0,.55),rgba(0,0,0,0) 60%)}
.hero-copy{position:absolute;left:104px;top:200px;color:#fff;width:560px}
.hero-copy h1{font-family:'Cinzel',serif;font-size:60px;font-weight:400;letter-spacing:3px}
.hero-copy p{font-size:15px;line-height:1.5;margin:10px 0 26px}
.dots{position:absolute;bottom:18px;left:50%;transform:translateX(-50%);display:flex;gap:10px}
.dots i{width:10px;height:10px;border-radius:50%;background:rgba(255,255,255,.5)}
.dots i:first-child{background:#fff}

/* welcome */
.welcome{height:520px;position:relative}
.welcome-copy{position:absolute;left:120px;top:100px;width:330px}
.welcome-copy .eyebrow{font-size:14px;letter-spacing:1px}
.welcome-copy h2{font-family:'Cinzel',serif;font-size:32px;margin:4px 0 16px}
.welcome-copy p{font-size:13px;line-height:1.6;color:var(--muted);margin-bottom:22px}
.welcome .img-a{position:absolute;left:632px;top:100px;width:268px;height:340px;background:linear-gradient(160deg,#3b2a1e,#8a5a2b 45%,#c89a52 60%,#2d1c12)}
.welcome .img-b{position:absolute;left:820px;top:78px;width:150px;height:280px;background:linear-gradient(170deg,#6b2a18,#c4622b 40%,#2b5d7a 70%,#5a1f14);border:6px solid var(--cream)}

/* categories */
.categories{height:640px;padding-top:12px}
.cat-row{display:flex;justify-content:space-between;margin-top:48px}
.cat{width:390px;height:520px;position:relative}
.cat .label{position:absolute;left:40px;bottom:40px;width:300px;height:66px;color:#fff;font-size:26px;font-weight:700;display:flex;align-items:center;justify-content:center}
.cat1{background:linear-gradient(150deg,#1c4f8a,#c64b2a 40%,#e0b34a 65%,#2b6c88)}
.cat2{background:linear-gradient(150deg,#2a1a10,#d98a2a 40%,#f4cc6a 55%,#5a2a14)}
.cat3{background:linear-gradient(150deg,#8a2a2a,#2b7a6a 35%,#e0a43a 60%,#5a1f3a)}
.cat1 .label{background:var(--purple)}
.cat2 .label{background:var(--orange)}
.cat3 .label{background:var(--teal)}

/* products */
.products{height:1060px;padding-top:40px}
.grid{display:grid;grid-template-columns:repeat(3,320px);column-gap:20px;justify-content:center}
.products .grid{margin-top:44px;row-gap:24px}
.product .pimg{height:320px}
.product h3{font-size:17px;font-weight:700;margin:10px 0 6px}
.stars{color:var(--star);font-size:14px;letter-spacing:1px}
.stars small{color:#888;font-size:11px;margin-left:4px}
.price{font-size:22px;font-weight:700;margin:4px 0}
.addcart{color:var(--accent);font-size:12px;font-weight:700}
.p1{background:linear-gradient(140deg,#3a2a1a,#b88a3a 50%,#4a3420)}
.p2{background:linear-gradient(140deg,#f2f0ea,#d83a3a 35%,#2a7a3a 55%,#e8c43a)}
.p3{background:linear-gradient(140deg,#1a3a6a,#d8c04a 40%,#2a8aaa 70%,#7a2a2a)}
.p4{background:linear-gradient(140deg,#2a5aa8,#c83a4a 45%,#2a3a8a)}
.p5{background:linear-gradient(140deg,#3a3a5a,#d8a84a 40%,#8a5a3a 70%,#2a2a3a)}
.p6{background:linear-gradient(140deg,#e8c44a,#3a7ad8 35%,#d84a3a 65%,#2a8a6a)}

/* testimonials */
.testimonials{height:472px;padding-top:28px;position:relative}
.quotes{display:flex;justify-content:center;gap:40px;margin-top:40px}
.quote{width:300px;text-align:center}
.quote .qmark{font-family:'Cinzel',serif;color:var(--accent-dark);font-size:40px;font-weight:700;line-height:1}
.quote p{font-size:15px;line-height:1.55;margin:8px 0 10px}
.quote b{font-size:15px}
.arrow{position:absolute;top:225px}
.arrow.left{left:62px}.arrow.right{right:62px}

/* newsletter */
.newsletter{height:388px;position:relative;background:linear-gradient(120deg,#2a1a10,#5a3a20 40%,#3a2414 70%,#1a100a);color:#fff;text-align:center}
.newsletter .shade{position:absolute;inset:0;background:rgba(0,0,0,.35)}
.newsletter .inner{position:relative;padding-top:112px}
.newsletter h2{font-family:'Cinzel',serif;font-size:36px;font-weight:700;letter-spacing:1px}
.newsletter p{font-size:14px;margin:8px 0 24px}
.subscribe{margin:0 auto;width:620px;height:60px;background:#fff;border-radius:30px;display:flex;align-items:center;justify-content:space-between;padding:0 6px 0 26px}
.subscribe span{color:#999;font-size:14px}
.subscribe b{background:var(--accent);color:#fff;font-size:14px;padding:16px 40px;border-radius:26px}

/* blog */
.blog{height:728px;padding-top:108px}
.blog .grid{margin-top:40px}
.post .bimg{height:262px}
.post h3{font-size:15px;font-weight:700;margin:16px 0 8px;line-height:1.35}
.post .date{font-size:12px;color:var(--muted);display:flex;align-items:center;gap:6px}
.post p{font-size:13px;line-height:1.55;color:var(--muted);margin:8px 0}
.post .more{color:var(--accent);font-size:12px;font-weight:700}
.b1{background:linear-gradient(140deg,#5a0a0a,#d8283a 40%,#f0a43a 60%,#4a0a10)}
.b2{background:linear-gradient(140deg,#1a3a6a,#c83a2a 40%,#e8c84a 60%,#2a5a8a)}
.b3{background:linear-gradient(140deg,#e88a2a,#3a5a8a 40%,#c84a3a 70%,#f0d0a0)}

/* follow */
.follow{height:384px;padding-top:88px}
.strip{display:flex;margin-top:30px}
.strip div{width:240px;height:228px}
.f1{background:linear-gradient(150deg,#2a4a6a,#c89a5a 50%,#4a3a2a)}
.f2{background:linear-gradient(150deg,#3a2a1a,#a86a3a 50%,#e8d0a0)}
.f3{background:linear-gradient(150deg,#e8b43a,#2a6ad8 40%,#d83a3a 70%,#2a8a5a)}
.f4{background:linear-gradient(150deg,#2a2a2a,#d84a3a 35%,#3a8ad8 65%,#e8d83a)}
.f5{background:linear-gradient(150deg,#f0f0f0,#8a8a8a 50%,#2a2a2a)}

/* footer */
.footer{height:300px;background:var(--footer);color:#ddd;position:relative}
.fcols{display:flex;padding:40px 0 0 120px;gap:0}
.fcol h4{color:#fff;font-size:14px;font-weight:700;margin-bottom:16px;letter-spacing:.5px}
.fcol li{list-style:none;font-size:12px;line-height:2}
.fcol p{font-size:12px;line-height:1.7}
.fcol .contact{display:flex;align-items:center;gap:8px;font-size:12px;margin-top:8px}
.c1{width:196px}.c2{width:196px}.c3{width:380px}.c4{width:230px}
.fcol .email{width:200px;height:32px;background:#fff;border-radius:16px;display:flex;align-items:center;justify-content:space-between;padding:0 4px 0 12px;margin:12px 0}
.fcol .email span{color:#999;font-size:11px}
.fcol .email b{width:24px;height:24px;border-radius:50%;background:var(--accent)}
.social{display:flex;gap:10px}
.social i{width:30px;height:30px;border-radius:50%;border:1px solid #aaa}
.copyright{position:absolute;left:0;right:0;bottom:0;height:44px;border-top:1px solid #333;display:flex;align-items:center;justify-content:space-between;padding:0 120px;font-size:12px;color:#bbb}
.cards{display:flex;gap:8px}
.cards i{width:38px;height:22px;border-radius:3px;background:#555}
</style>
</head>
<body>

<div class="topbar">
  <span>Get 25% off discount code: HAND25</span>
  <div class="links">
    <span><svg width="13" height="13" viewBox="0 0 24 24"><path fill="#fff" d="M6.6 10.8a15 15 0 006.6 6.6l2.2-2.2a1 1 0 011-.25 11 11 0 003.6.6 1 1 0 011 1V20a1 1 0 01-1 1A17 17 0 013 4a1 1 0 011-1h3.5a1 1 0 011 1 11 11 0 00.6 3.6 1 1 0 01-.25 1z"/></svg>CALL (555) 014-2290</span>
    <span><svg width="13" height="13" viewBox="0 0 24 24"><circle cx="12" cy="8" r="4" fill="#fff"/><path fill="#fff" d="M4 21a8 8 0 0116 0z"/></svg>MY ACCOUNT</span>
    <span><svg width="13" height="13" viewBox="0 0 24 24"><circle cx="12" cy="8" r="4" fill="#fff"/><path fill="#fff" d="M4 21a8 8 0 0116 0z"/></svg>SIGN IN</span>
  </div>
</div>

<header class="header">
  <div class="logo"><span class="mark"></span><span class="name">Corvane Mart</span></div>
  <div class="search"><span>Search here...</span><b><svg width="16" height="16" viewBox="0 0 24 24"><circle cx="10" cy="10" r="6" fill="none" stroke="#fff" stroke-width="2.5"/><path d="M15 15l6 6" stroke="#fff" stroke-width="2.5"/></svg></b></div>
  <div class="cart"><svg width="28" height="28" viewBox="0 0 24 24"><path d="M3 4h3l2.5 11h10l2-8H7" fill="none" stroke="#222" stroke-width="1.8"/><circle cx="10" cy="19" r="1.5" fill="#222"/><circle cx="17" cy="19" r="1.5" fill="#222"/></svg><div>SHOPPING CART<small>0 items</small></div></div>
  <nav class="nav"><a>HOME</a><a>ABOUT US ▾</a><a>SHOP</a><a>BLOG</a><a>FAQ</a><a>CONTACT</a></nav>
</header>

<section class="hero" role="img" aria-label="Market stall shelves stacked with painted ceramic pots and lamps">
  <div class="shade"></div>
  <div class="hero-copy">
    <h1>Corvane Mart</h1>
    <p>Handmade goods from makers across the old markets, gathered in one place for you to browse, choose and bring home today.</p>
    <a class="btn">SHOP NOW</a>
  </div>
  <div class="dots"><i></i><i></i><i></i></div>
</section>

<section class="welcome">
  <div class="welcome-copy">
    <div class="eyebrow">WELCOME TO</div>
    <h2>Corvane Mart</h2>
    <p>We bring together craft makers from the Saffron Quarter and the Copperleaf Arcade. Every lamp, bowl and rug is made by hand and sold straight from the maker's own workshop. Browse by category, follow your favourite makers and find a piece with a story behind it for your home or as a gift.</p>
    <a class="btn">READ MORE</a>
  </div>
  <div class="img-a photo" role="img" aria-label="Hanging brass lanterns in a market shop"></div>
  <div class="img-b photo" role="img" aria-label="Colourful handmade goods on display"></div>
</section>

<section class="categories">
  <h2 class="section-title">Featured Categories</h2>
  <div class="cat-row">
    <div class="cat cat1" role="img" aria-label="Stacks of hand-painted ceramic bowls"><div class="label">Finibus Bonorum</div></div>
    <div class="cat cat2" role="img" aria-label="Glowing mosaic glass lamps"><div class="label">Finibus Bonorum</div></div>
    <div class="cat cat3" role="img" aria-label="Woven textiles and rugs"><div class="label">Finibus Bonorum</div></div>
  </div>
</section>

<section class="products">
  <h2 class="section-title">Featured Products</h2>
  <div class="grid">
    <div class="product"><div class="pimg p1" role="img" aria-label="Brass teapots and trays"></div><h3>The standard Lorem Ipsum</h3><div class="stars">★★★★★<small>(10)</small></div><div class="price">$289</div><div class="addcart">ADD TO CART 🛒</div></div>
    <div class="product"><div class="pimg p2" role="img" aria-label="Beaded bracelets"></div><h3>The standard Lorem Ipsum</h3><div class="stars">★★★★★<small>(10)</small></div><div class="price">$289</div><div class="addcart">ADD TO CART 🛒</div></div>
    <div class="product"><div class="pimg p3" role="img" aria-label="Mosaic glass lamps"></div><h3>The standard Lorem Ipsum</h3><div class="stars">★★★★★<small>(10)</small></div><div class="price">$289</div><div class="addcart">ADD TO CART 🛒</div></div>
    <div class="product"><div class="pimg p4" role="img" aria-label="Painted ceramic vases"></div><h3>The standard Lorem Ipsum</h3><div class="stars">★★★★★<small>(10)</small></div><div class="price">$289</div><div class="addcart">ADD TO CART 🛒</div></div>
    <div class="product"><div class="pimg p5" role="img" aria-label="Metal lanterns"></div><h3>The standard Lorem Ipsum</h3><div class="stars">★★★★★<small>(10)</small></div><div class="price">$289</div><div class="addcart">ADD TO CART 🛒</div></div>
    <div class="product"><div class="pimg p6" role="img" aria-label="Decorated plates"></div><h3>The standard Lorem Ipsum</h3><div class="stars">★★★★★<small>(10)</small></div><div class="price">$289</div><div class="addcart">ADD TO CART 🛒</div></div>
  </div>
</section>

<section class="testimonials">
  <h2 class="section-title">What Our Customers Say</h2>
  <svg class="arrow left" width="14" height="22" viewBox="0 0 14 22"><path d="M12 2L3 11l9 9" fill="none" stroke="#333" stroke-width="3"/></svg>
  <svg class="arrow right" width="14" height="22" viewBox="0 0 14 22"><path d="M2 2l9 9-9 9" fill="none" stroke="#333" stroke-width="3"/></svg>
  <div class="quotes">
    <div class="quote"><div class="stars">★★★★★</div><div class="qmark">“</div><p>Lorem ipsum dolor sit amet, consectetur adipiscing elit, sed do eiusmod tempor incididunt ut labore et dolore.</p><b>– Mara Ellison</b></div>
    <div class="quote"><div class="stars">★★★★★</div><div class="qmark">“</div><p>Lorem ipsum dolor sit amet, consectetur adipiscing elit, sed do eiusmod tempor incididunt ut labore et dolore.</p><b>– Mara Ellison</b></div>
    <div class="quote"><div class="stars">★★★★★</div><div class="qmark">“</div><p>Lorem ipsum dolor sit amet, consectetur adipiscing elit, sed do eiusmod tempor incididunt ut labore et dolore.</p><b>– Mara Ellison</b></div>
  </div>
</section>

<section class="newsletter" role="img" aria-label="Dim market street lit by hanging lanterns">
  <div class="shade"></div>
  <div class="inner">
    <h2>Subscribe to our Newsletter</h2>
    <p>A short note each week with new makers and offers sent to your inbox</p>
    <div class="subscribe"><span>Enter Your Email Address</span><b>SUBSCRIBE</b></div>
  </div>
</section>

<section class="blog">
  <h2 class="section-title">Latest Blog</h2>
  <div class="grid">
    <div class="post"><div class="bimg b1" role="img" aria-label="Red lanterns in a market alley"></div><h3>LOREM IPSUM DOLOR SIT AMET, CONSECTETUR ADIPISCING</h3><div class="date">📅 May 12, 2023</div><p>Lorem ipsum dolor sit amet, consectetur adipiscing elit, sed do eiusmod tempor incididunt ut labore et dolore magna aliqua.</p><a class="more">Learn More ›</a></div>
    <div class="post"><div class="bimg b2" role="img" aria-label="Painted ceramic dishes"></div><h3>LOREM IPSUM DOLOR SIT AMET, CONSECTETUR ADIPISCING</h3><div class="date">📅 May 12, 2023</div><p>Lorem ipsum dolor sit amet, consectetur adipiscing elit, sed do eiusmod tempor incididunt ut labore et dolore magna aliqua.</p><a class="more">Learn More ›</a></div>
    <div class="post"><div class="bimg b3" role="img" aria-label="Market stall with woven goods"></div><h3>LOREM IPSUM DOLOR SIT AMET, CONSECTETUR ADIPISCING</h3><div class="date">📅 May 12, 2023</div><p>Lorem ipsum dolor sit amet, consectetur adipiscing elit, sed do eiusmod tempor incididunt ut labore et dolore magna aliqua.</p><a class="more">Learn More ›</a></div>
  </div>
</section>

<section class="follow">
  <h2 class="section-title">Follow @Corvane Mart</h2>
  <div class="strip">
    <div class="f1" role="img" aria-label="Market archway"></div>
    <div class="f2" role="img" aria-label="Craft workshop"></div>
    <div class="f3" role="img" aria-label="Painted bowls"></div>
    <div class="f4" role="img" aria-label="Beaded goods"></div>
    <div class="f5" role="img" aria-label="White pottery"></div>
  </div>
</section>

<footer class="footer">
  <div class="fcols">
    <div class="fcol c1"><h4>QUICK LINKS</h4><ul><li>Search</li><li>Become a Seller</li><li>Contact Us</li><li>Refund Policy</li><li>Shipping Policy</li><li>Privacy Policy</li><li>Terms of Service</li></ul></div>
    <div class="fcol c2"><h4>MAIN MENU</h4><ul><li>Home</li><li>About Us</li><li>Shop</li><li>Blog</li><li>Faq</li><li>Contact</li></ul></div>
    <div class="fcol c3"><h4>PURCHASING &amp; DISTRIBUTION</h4><p>Questions about orders, wholesale or shipping? Our team answers every message within one working day.</p>
      <div class="contact">✉ hello@corvanemart.com</div>
      <div class="contact">☎ (555) 014-2290</div>
      <div class="contact">⌖ 12 Lantern Row, Fenwick TX 75001</div></div>
    <div class="fcol c4"><h4>NEWS &amp; UPDATES</h4><p>Sign up to get the latest on sales, new makers and more …</p>
      <div class="email"><span>Enter your email</span><b></b></div>
      <div class="social"><i></i><i></i><i></i><i></i></div></div>
  </div>
  <div class="copyright"><span>Copyright © 2023 Corvane Mart. All Rights Reserved.</span><div class="cards"><i></i><i></i><i></i><i></i><i></i></div></div>
</footer>

</body>
</html>
```